Beer Can Label named: ZAP Ginger Beer

We need a funky design for a Ginger Beer that is made from all natural ingredients. The label needs to be full of Colour, emphasis on the Ginger Root. ZAP (Zested And Poured)

Target Market(s)

None beer drinkers'

Requirements
Must have
• Name on the label must beer easy to read. Needs to be very colourful, playful & even a bit cheaky.
Nice to have
• A label that looks at the benefits of Ginger for the body in a fun artistic design.
Should not have
• Should NOT be a simple, basic, minimalistic design

```html
<!DOCTYPE html>
<html lang="en">
<head>
<meta charset="utf-8">
<title>ZAP Ginger Beer – Label Colourways</title>
<link rel="stylesheet" href="https://fonts.googleapis.com/css2?family=Alfa+Slab+One&family=Arvo:wght@700&display=swap">
<style>
  :root {
    --page-bg: #ffffff;
    --red-top: #e4120c;
    --red-mid: #f2400f;
    --orange: #f7961a;
    --amber: #fbb829;
    --yellow-top: #fff200;
    --yellow-mid: #ffd21a;
    --cream: #fbf6ec;
    --brown: #5a2e10;
    --maroon: #7a1508;
    --foam: #fff3c4;
    --ginger-light: #e2c27d;
    --ginger-dark: #b88a3e;
    --ink: #3a1d0a;
  }
  * { box-sizing: border-box; margin: 0; padding: 0; }
  html, body {
    width: 1200px; height: 1200px; overflow: hidden;
    background: var(--page-bg);
  }
  .canvas {
    position: relative; width: 1200px; height: 1200px;
    display: flex; justify-content: center; align-items: center; gap: 60px;
  }
  .label {
    position: relative; width: 510px; height: 780px; overflow: hidden;
    text-align: center;
  }
  .label--red {
    --title-colour: var(--cream);
    background: linear-gradient(180deg, var(--red-top) 0%, var(--red-mid) 40%, var(--orange) 75%, var(--amber) 100%);
  }
  .label--yellow {
    --title-colour: var(--brown);
    background: linear-gradient(180deg, var(--yellow-top) 0%, var(--yellow-mid) 35%, var(--orange) 75%, var(--amber) 100%);
  }
  .label__title {
    position: absolute; top: 44px; left: 0; right: 0;
    font-family: "Alfa Slab One", serif; font-weight: 400;
    color: var(--title-colour);
    line-height: 1;
  }
  .label__title-top { display: block; font-size: 64px; }
  .label__title-bottom { display: block; font-size: 104px; }
  .label__name {
    position: absolute; top: 238px; left: 0; right: 0;
    font-family: "Alfa Slab One", serif;
    font-size: 170px; line-height: 1; letter-spacing: 6px;
    color: var(--maroon);
  }
  .label__liquid {
    position: absolute; left: 0; right: 0; top: 452px; bottom: 0;
    background: linear-gradient(180deg, rgba(255,190,60,0.55) 0%, rgba(250,150,30,0.35) 60%, rgba(251,184,41,0.2) 100%);
  }
  .label__foam {
    position: absolute; left: 0; right: 0; top: 440px; height: 24px;
    background: linear-gradient(180deg, rgba(255,243,196,0) 0%, var(--foam) 45%, rgba(255,243,196,0) 100%);
    opacity: 0.85;
  }
  .label__ginger {
    position: absolute; left: 165px; top: 462px; width: 180px; height: 180px;
    border-radius: 46% 54% 42% 58% / 50% 44% 56% 50%;
    background: radial-gradient(ellipse at 45% 40%, var(--ginger-light) 0%, var(--ginger-dark) 100%);
  }
  .label__origin {
    position: absolute; top: 664px; left: 0; right: 0;
    font-family: "Arvo", serif; font-weight: 700; font-size: 34px;
    color: var(--cream);
  }
  .label__volume {
    position: absolute; top: 732px; left: 0; right: 0;
    font-family: "Arvo", serif; font-weight: 700; font-size: 19px;
    color: var(--ink);
  }
</style>
</head>
<body>
<main class="canvas">
  <section class="label label--red" aria-label="ZAP Ginger Beer label, red colourway">
    <h1 class="label__title"><span class="label__title-top">Ginger Root</span><span class="label__title-bottom">Beer</span></h1>
    <div class="label__name">ZAP</div>
    <div class="label__liquid" role="img" aria-label="Sparkling ginger beer liquid with bubbles"></div>
    <div class="label__foam"></div>
    <div class="label__ginger" role="img" aria-label="Illustration of a fresh ginger root splashing into the drink"></div>
    <p class="label__origin">Zested And Poured</p>
    <p class="label__volume">12 fluid ounces</p>
  </section>

  <section class="label label--yellow" aria-label="ZAP Ginger Beer label, yellow colourway">
    <h1 class="label__title"><span class="label__title-top">Ginger Root</span><span class="label__title-bottom">Beer</span></h1>
    <div class="label__name">ZAP</div>
    <div class="label__liquid" role="img" aria-label="Sparkling ginger beer liquid with bubbles"></div>
    <div class="label__foam"></div>
    <div class="label__ginger" role="img" aria-label="Illustration of a fresh ginger root splashing into the drink"></div>
    <p class="label__origin">Zested And Poured</p>
    <p class="label__volume">12 fluid ounces</p>
  </section>
</main>
</body>
</html>
```